Kalmoret Windham & Associates

We would like a simple, professional business card using a similar font to our logo.

Industry/Entity Type

Law Firm

Contact Information for Business Card

Martin Kalmoret, Esq. 47 Tillman Lane, 2nd Floor Alderbrook, VT 05999 Office: 781.555.0143 Cell: 508.555.0196 Email: marty@kwfirmma.com kalmoretwindhamlaw.com

Font styles to use
Other font styles liked:
• We would like to use the fonts used in the logo or similar

Colors
0054AA
0677BA
7BADD7
CADEEF
E8F1F8

Requirements
Must have
• We would like the fonts to match the logo
Nice to have
• not too much design- very simple and professional business card. I added a picture of a business card that I tried to start but I am not a designer! Hopefully it will help with the address and phone numbers and kind of what we are looking for.

```html
<!DOCTYPE html>
<html lang="en">
<head>
<meta charset="utf-8">
<title>Kalmoret Windham &amp; Associates – Business Card</title>
<link rel="stylesheet" href="https://fonts.googleapis.com/css2?family=Cinzel:wght@400;500&family=Roboto:wght@300;400&display=swap">
<style>
  :root {
    --navy: #1f3770;
    --white: #ffffff;
    --ink: #3d3f46;
    --backdrop: #e9e6e0;
  }
  * { box-sizing: border-box; margin: 0; padding: 0; }
  html, body { width: 1200px; height: 1040px; overflow: hidden; }
  body {
    background: var(--backdrop);
    position: relative;
    font-family: "Roboto", sans-serif;
  }
  .card {
    position: absolute;
    width: 700px;
    height: 400px;
    box-shadow: 0 6px 18px rgba(0,0,0,0.18);
  }
  .card-front { left: 90px; top: 80px; background: var(--white); }
  .card-back { left: 410px; top: 560px; background: var(--navy); }

  .firm-mark {
    position: absolute;
    display: flex;
    align-items: center;
    gap: 16px;
  }
  .firm-mark .mark-square {
    width: 70px; height: 70px;
    flex: none;
  }
  .firm-mark .firm-name {
    font-family: "Cinzel", serif;
    font-weight: 500;
    line-height: 1.05;
    text-transform: uppercase;
    white-space: nowrap;
  }
  .card-front .firm-mark { left: 50px; top: 150px; }
  .card-front .mark-square { background: var(--navy); }
  .card-front .firm-name { color: var(--navy); font-size: 21px; }

  .card-back .firm-mark { left: 50%; top: 50%; transform: translate(-50%, -50%); }
  .card-back .mark-square { background: var(--white); width: 96px; height: 96px; }
  .card-back .firm-name { color: var(--white); font-size: 30px; }

  .contact-block {
    position: absolute;
    left: 380px;
    top: 50px;
  }
  .person-name {
    font-family: "Cinzel", serif;
    font-weight: 500;
    font-size: 25px;
    color: var(--navy);
    letter-spacing: 0.5px;
    margin-bottom: 14px;
    white-space: nowrap;
  }
  .contact-row {
    display: flex;
    align-items: flex-start;
    gap: 10px;
    font-size: 14px;
    font-weight: 300;
    color: var(--ink);
    line-height: 1.45;
    white-space: nowrap;
  }
  .contact-row svg { width: 12px; height: 12px; margin-top: 4px; flex: none; fill: var(--navy); }
  .contact-group { margin-bottom: 8px; }

  .web-band {
    position: absolute;
    left: 40px;
    right: 12px;
    bottom: 22px;
    height: 50px;
    background: var(--navy);
    display: flex;
    align-items: center;
    justify-content: center;
    color: var(--white);
    font-size: 16px;
    letter-spacing: 3px;
  }
  .web-band strong { font-weight: 400; }
</style>
</head>
<body>

<section class="card card-front" aria-label="Business card front">
  <div class="firm-mark">
    <span class="mark-square"></span>
    <span class="firm-name">Kalmoret<br>Windham<br>&amp; Associates</span>
  </div>

  <div class="contact-block">
    <h1 class="person-name">Martin Kalmoret</h1>
    <div class="contact-group">
      <div class="contact-row">
        <svg viewBox="0 0 12 12"><path d="M6 0a4 4 0 0 0-4 4c0 3 4 8 4 8s4-5 4-8a4 4 0 0 0-4-4zm0 5.5A1.5 1.5 0 1 1 6 2.5a1.5 1.5 0 0 1 0 3z"/></svg>
        <span>Esq. 47 Tillman Lane<br>2nd Floor<br>Alderbrook, VT 05999</span>
      </div>
    </div>
    <div class="contact-row">
      <svg viewBox="0 0 12 12"><path d="M2.5 0.5l2 2.5-1.2 1.3c.7 1.6 2 2.9 3.6 3.6L8.2 6.7l2.5 2-1.2 2.3C5 11 1 7 0.7 2.2z"/></svg>
      <span>781.555.0143</span>
    </div>
    <div class="contact-row">
      <svg viewBox="0 0 12 12"><path d="M3 0h6v12H3zM4 1.2v8.3h4V1.2z"/></svg>
      <span>508.555.0196</span>
    </div>
    <div class="contact-row">
      <svg viewBox="0 0 12 12"><path d="M0 2h12v8H0zm1 1l5 3.5L11 3z"/></svg>
      <span>marty@kwfirmma.com</span>
    </div>
  </div>

  <div class="web-band">www.<strong>KalmoretWindhamLaw</strong>.com</div>
</section>

<section class="card card-back" aria-label="Business card back">
  <div class="firm-mark">
    <span class="mark-square"></span>
    <span class="firm-name">Kalmoret<br>Windham<br>&amp; Associates</span>
  </div>
</section>

</body>
</html>
```